Design a building access mobile app for Tally by Halvorn Portal Systems

Hello, We're looking for an awesome designer to create an app design for our app Tally, by Halvorn Portal Systems. the mobile app allows employees open their office doors with their mobile phone. this means they don't have to use those plastic card badges or keys. We like clean modern design, dark and light themes. We don't have a logo yet.
Updates

Reason: Waiting on a couple designers to submit concepts

Target Market(s)

Commercial and employees

Industry/Entity Type

Building

Font styles to use
Sans Serif
Other font styles liked:
• Oswald extra light

Requirements
Must have
• nice clean design

```html
<!DOCTYPE html>
<html lang="en">
<head>
<meta charset="utf-8">
<title>Tally – Door Access</title>
<link rel="stylesheet" href="https://fonts.googleapis.com/css2?family=Oswald:wght@200;300&family=Roboto:wght@400;500&display=swap">
<style>
  :root {
    --brand-blue: #38c6ee;
    --white: #ffffff;
    --field-bg: #f2f2f2;
    --field-text: #b5b5b5;
    --icon-grey: #a6a6a6;
    --label-grey: #9a9a9a;
    --ring: #d6d6d6;
    --dial-bg: #f2f2f2;
    --arrow-left: #cfcfcf;
    --arrow-right: #a0a0a0;
    --version: #b0b0b0;
  }
  * { box-sizing: border-box; margin: 0; padding: 0; }
  html, body { width: 675px; height: 1200px; overflow: hidden; background: var(--white); }
  .app { position: relative; width: 675px; height: 1200px; overflow: hidden; font-family: 'Oswald', sans-serif; }

  .backdrop {
    position: absolute; left: 0; top: 112px; width: 675px; height: 1088px;
    background: linear-gradient(160deg, #fbfbfb 0%, #ffffff 35%, #fafafa 70%, #fdfdfd 100%);
  }

  .top-bar { position: absolute; left: 0; top: 0; width: 675px; height: 112px; background: var(--brand-blue); color: var(--white); }
  .status { position: absolute; left: 0; top: 0; width: 100%; height: 40px; font-family: 'Roboto', sans-serif; font-weight: 500; font-size: 16px; }
  .status-time { position: absolute; left: 0; width: 100%; top: 10px; text-align: center; }
  .status-signal { position: absolute; left: 10px; top: 12px; }
  .status-right { position: absolute; right: 10px; top: 10px; display: flex; align-items: center; gap: 5px; }

  .menu-btn { position: absolute; left: 23px; top: 62px; }
  .info-btn { position: absolute; right: 22px; top: 59px; }
  .app-title { position: absolute; left: 0; width: 100%; top: 49px; text-align: center; font-weight: 300; font-size: 32px; line-height: 46px; letter-spacing: 0.2px; }

  .location-field {
    position: absolute; left: 50px; top: 174px; width: 576px; height: 74px;
    background: var(--field-bg); border-radius: 4px; box-shadow: 0 1px 2px rgba(0,0,0,0.06);
  }
  .location-placeholder { position: absolute; left: 24px; top: 0; line-height: 74px; font-weight: 200; font-size: 29px; color: var(--field-text); }
  .location-pin { position: absolute; right: 18px; top: 19px; }

  .dial {
    position: absolute; left: 157px; top: 419px; width: 362px; height: 362px;
    border-radius: 50%; background: var(--dial-bg); border: 2px solid var(--ring);
  }
  .dial-icon { position: absolute; left: 130px; top: 75px; }
  .dial-label { position: absolute; left: 0; width: 100%; top: 240px; text-align: center; font-weight: 300; font-size: 40px; color: var(--label-grey); }

  .nav-arrow { position: absolute; top: 578px; }
  .nav-prev { left: 113px; }
  .nav-next { left: 536px; }

  .version { position: absolute; left: 0; width: 100%; top: 1152px; text-align: center; font-weight: 200; font-size: 22px; color: var(--version); }
</style>
</head>
<body>
<main class="app">
  <div class="backdrop" role="img" aria-label="Faint photo of a bright office corridor"></div>

  <header class="top-bar">
    <div class="status">
      <svg class="status-signal" width="68" height="14" viewBox="0 0 68 14">
        <g fill="#fff"><circle cx="5" cy="6" r="4"/><circle cx="15" cy="6" r="4"/><circle cx="25" cy="6" r="4"/><circle cx="35" cy="6" r="4"/><circle cx="45" cy="6" r="4"/></g>
        <path d="M53 4 a10 10 0 0 1 14 0 M55.5 7 a6 6 0 0 1 9 0" stroke="#fff" stroke-width="2" fill="none"/>
        <circle cx="60" cy="11" r="2" fill="#fff"/>
      </svg>
      <div class="status-time">9:41 PM</div>
      <div class="status-right">
        <svg width="10" height="18" viewBox="0 0 10 18"><path d="M1 5 L8 12 L4.5 15.5 V2.5 L8 6 L1 13" stroke="rgba(255,255,255,0.75)" stroke-width="1.4" fill="none"/></svg>
        <span>100%</span>
        <svg width="32" height="16" viewBox="0 0 32 16"><rect x="1" y="1" width="27" height="14" rx="3" stroke="#fff" stroke-width="1.5" fill="none"/><rect x="3" y="3" width="23" height="10" rx="1.5" fill="#fff"/><rect x="29.5" y="5.5" width="2" height="5" rx="1" fill="#fff"/></svg>
      </div>
    </div>
    <svg class="menu-btn" width="33" height="22" viewBox="0 0 33 22"><g stroke="#fff" stroke-width="2.4"><line x1="0" y1="2" x2="33" y2="2"/><line x1="0" y1="11" x2="33" y2="11"/><line x1="0" y1="20" x2="33" y2="20"/></g></svg>
    <h1 class="app-title">Halvorn Security</h1>
    <svg class="info-btn" width="28" height="28" viewBox="0 0 28 28"><circle cx="14" cy="14" r="12.5" stroke="#fff" stroke-width="1.8" fill="none"/><circle cx="14" cy="8.5" r="1.4" fill="#fff"/><line x1="14" y1="12" x2="14" y2="21" stroke="#fff" stroke-width="1.8"/></svg>
  </header>

  <div class="location-field">
    <span class="location-placeholder">Enter your office location</span>
    <svg class="location-pin" width="28" height="36" viewBox="0 0 28 36"><path d="M14 1 C6.8 1 1 6.6 1 13.6 C1 22.5 14 35 14 35 S27 22.5 27 13.6 C27 6.6 21.2 1 14 1 Z" fill="var(--icon-grey)"/><circle cx="14" cy="13.5" r="5" fill="var(--field-bg)"/></svg>
  </div>

  <svg class="nav-arrow nav-prev" width="26" height="44" viewBox="0 0 26 44"><polyline points="24,2 3,22 24,42" stroke="var(--arrow-left)" stroke-width="2" fill="none"/></svg>

  <div class="dial">
    <svg class="dial-icon" width="100" height="160" viewBox="0 0 100 160">
      <path d="M5 155 V5 H95 V153" stroke="var(--icon-grey)" stroke-width="7" fill="none" stroke-linejoin="round" stroke-linecap="round"/>
      <polygon points="52,36 96,6 96,130 52,157" fill="var(--icon-grey)"/>
      <circle cx="64" cy="93" r="4" fill="var(--dial-bg)"/>
      <line x1="56" y1="93" x2="64" y2="93" stroke="var(--dial-bg)" stroke-width="2"/>
    </svg>
    <div class="dial-label">Door</div>
  </div>

  <svg class="nav-arrow nav-next" width="26" height="44" viewBox="0 0 26 44"><polyline points="2,2 23,22 2,42" stroke="var(--arrow-right)" stroke-width="2" fill="none"/></svg>

  <div class="version">v 2.0.1</div>
</main>
</body>
</html>
```